Weather of the Heart Is the Ledger A Novel by Carl Whitby and Martin Holloway

Weather of the Heart Is the Ledger is a business novel about leadership, follower-ship, resilience, and insight.
It follows a high-performing executive whose conventional management tools and techniques stop working during a professional crisis. His transformation does not come from new strategies or tactics, but from a fundamentally different understanding of how mindset shapes performance, decision-making, leadership and follower-ship. Through the course of the book, the executive, his team, and his customers realize that “State of Mind” (healthy psychological functioning) is the horsepower that drives business and life.
This is not a self-help book, textbook, or memoir. It is thoughtful business fiction with philosophical depth.

Introduction/Preface for the novel:
We wrote this book because something profound changed the way we live, work, and lead. Over the course of several decades - across boardrooms, high-stakes corporate challenges, private practice, and moments of quiet personal insight - we began to see a deeper truth about the human experience. It was a truth that, once seen, dramatically improved the quality of our lives, and the lives of the people with whom we worked.
That truth comes from understanding the Three Principles of Mind, Consciousness, and Thought, as discovered and first articulated by the philosopher and theosopher, Edwin Thorley. Though simple, these Principles point to something universally powerful—how all people experience life from the inside out. When understood, they reveal a level of clarity, resilience, and well-being that can transform not only individuals, but entire organizations.
At first, we tried to write a traditional business book—a primer designed to share how understanding the Principles can lead to more grounded, wise, and effective leadership—without the need for techniques or tools. But as we wrote, we found ourselves returning again and again to stories. Real stories. Composite stories. Fictional ones. We realized that the best way to share this understanding wasn’t through frameworks or prescriptive advice. It was through story.
So, we created one big story.
This novel is the result. Though fictional, it is inspired by real patterns, real shifts, and real struggles we’ve lived through and witnessed over decades of work, together and separately. The characters are inventions, but their experiences are familiar. We’ve watched people just like them transform—from confusion to clarity, from fear to resilience, from burnout to wisdom.
Our hope is that this book moves you—not just as a story, but as an experience. We believe that the ideas woven into Owen Castell’s journey can help anyone live with greater ease, purpose, and peace of mind. Whether you lead a Fortune 500 company or a family of five, what’s offered here is for you.
And if something in this story helps you see your own life with fresh eyes, then the book has done its job.
Welcome to the journey.
—Carl & Martin

Target Market(s)

• Senior leaders, executives, and high-potential managers • Business professionals experiencing pressure, burnout, or diminishing returns from traditional leadership approaches • Leadership coaches and organizational consultants • Readers of intelligent, reflective business fiction or non-business people who are interested in what makes people tick — and achieve their highest potential Tone should appeal to serious, experienced professionals, not beginners or hype-seekers.

Industry/Entity Type

• Business / Leadership / Psychology • Business Fiction • Leadership Novel

Font styles to use
Serif

Colors
0054AA
0677BA
7BADD7
CADEEF
E8F1F8

Requirements
Must have
• We are looking for metaphorical representations of: • A fork in the road • A deviation from the conventional path (that makes all the difference) • One element choosing a different direction—not running away, not rebelling, just seeing differently Think quiet insight, not drama. Must-Haves • Clear, legible title at thumbnail size • A visual metaphor for choice or alternate thinking • Professional, credible aesthetic • Obvious that this is fiction (a novel), not a textbook • Clean typography (no clutter)
Nice to have
• • A sense of motion or transition • Minimalist or restrained color palette • One accent element that signifies insight or departure from convention • Timeless design (should still feel current in 5 or 10 years)
Should not have
• • Literal business clichés (gears, ladders, chess pieces, lightbulbs, compasses, eagles) • Stock-photo people in suits • “Hero CEO” imagery • Overly mystical or “woo-woo” visuals • Aggressive, macho, or hustle-culture tone • Anything cartoonish or silly

```html
<!DOCTYPE html>
<html lang="en">
<head>
<meta charset="utf-8">
<title>Weather of the Heart Is the Ledger — Cover</title>
<link href="https://fonts.googleapis.com/css2?family=Bodoni+Moda:opsz,wght@6..96,700;6..96,800&family=Questrial&display=swap" rel="stylesheet">
<style>
  :root {
    --sky: #CADEEF;
    --ink: #0677BA;
    --path: #6FA7DB;
  }
  html, body {
    margin: 0;
    padding: 0;
    width: 800px;
    height: 1200px;
    overflow: hidden;
    background: var(--sky);
  }
  .cover {
    display: block;
    width: 800px;
    height: 1200px;
  }
  .cover-bg { fill: var(--sky); }
  .path-line {
    fill: none;
    stroke: var(--path);
    stroke-width: 6;
  }
  .title-main {
    font-family: "Bodoni Moda", "Didot", serif;
    font-weight: 800;
    font-size: 128px;
    fill: var(--ink);
  }
  .title-small {
    font-family: "Bodoni Moda", "Didot", serif;
    font-weight: 700;
    font-size: 34px;
    fill: var(--ink);
  }
  .byline {
    font-family: "Questrial", "Century Gothic", sans-serif;
    font-size: 17px;
    fill: var(--ink);
  }
</style>
</head>
<body>
<svg class="cover" viewBox="0 0 800 1200" xmlns="http://www.w3.org/2000/svg" role="img" aria-label="Weather of the Heart Is the Ledger, a novel by Carl Whitby and Martin Holloway">
  <rect class="cover-bg" x="0" y="0" width="800" height="1200"/>

  <!-- the path that bends away -->
  <path class="path-line" d="M596,-2 C572,120 558,290 553.6,467"/>
  <line class="path-line" x1="553.6" y1="668" x2="553.6" y2="778"/>
  <line class="path-line" x1="553.6" y1="802" x2="553.6" y2="1202"/>

  <!-- title -->
  <g class="title">
    <text class="title-main" x="122" y="562" textLength="556" lengthAdjust="spacingAndGlyphs">WEATHER OF THE HEART</text>
    <text class="title-small" transform="translate(159 571) rotate(90)" x="0" y="0" textLength="88" lengthAdjust="spacingAndGlyphs">IS THE</text>
    <text class="title-main" x="192" y="661" textLength="521" lengthAdjust="spacingAndGlyphs">LEDGER</text>
  </g>

  <!-- byline -->
  <text class="byline" x="400" y="795" text-anchor="middle">A Novel by Carl Whitby and Martin Holloway</text>
</svg>
</body>
</html>
```